Home Refinance . Residential Mortgages

I want to post a small flyer as part of an email. I want do an email blast. I am a mortgage company and want to entice borrowers with my low interest rates. My website is www.oakmerecapital-demo.com
The colors must match the website colors.
VA IRRL REFINANCE.
30 YR. FIXED RATES as low as
2.25% | 2.437% APR
No Appraisal, No out of Pocket cost, NO Income Verification, NO Asset Verification, Close in 30 days or less

Target Market(s)

Real Estate agents & Borrowers looking to get a mortgage loan

Colors
0455a3
ec1f27
28a1d5

Requirements
Must have
• The colors must match the website colors.
OAKMERE CAPITAL, INC,.
4817B Wellsbury Road
Alexandria, VA 22987
QRLA 5830724
www.qrlaborrowerlookup-demo.com

Bright Harbor Pledge LOGO.

```html
<!DOCTYPE html>
<html lang="en">
<head>
<meta charset="utf-8">
<title>Oakmere Capital – VA IRRL Refinance</title>
<link rel="stylesheet" href="https://fonts.googleapis.com/css2?family=Oswald:wght@500;600&family=Montserrat:wght@600;700;800&family=Roboto:wght@400&display=swap">
<style>
  :root {
    --blue: #0455a3;
    --navy: #0b3a82;
    --red: #ec1f27;
    --crimson: #c8102e;
    --sky: #28a1d5;
    --ink: #1d1d1f;
    --paper: #ffffff;
    --mist: #eef0f3;
    --stage: #2b2b2b;
  }
  * { margin: 0; padding: 0; box-sizing: border-box; }
  html, body { width: 1200px; height: 613px; overflow: hidden; background: var(--stage); }
  .flyer {
    position: absolute; left: 397px; top: 20px; width: 405px; height: 573px;
    background: var(--paper); overflow: hidden;
    box-shadow: 0 6px 18px rgba(0,0,0,.45);
    font-family: "Montserrat", sans-serif;
  }
  .hero-photo {
    position: absolute; left: 0; top: 0; width: 405px; height: 280px;
    background: linear-gradient(100deg, #8a7a5c 0%, #c9a86a 30%, #e8d6b0 55%, #f6ecd9 75%, #fbf4e6 100%);
  }
  .shapes { position: absolute; left: 0; top: 0; }
  .brand {
    position: absolute; right: 22px; top: 22px; display: flex; align-items: center; gap: 6px;
    font-family: "Roboto", sans-serif; font-size: 19px; color: var(--ink);
  }
  .brand-mark { width: 14px; height: 14px; background: var(--blue); }
  .services {
    position: absolute; right: 20px; top: 60px; text-align: right;
    font-family: "Oswald", sans-serif; font-weight: 600; font-size: 23px; line-height: 24px;
  }
  .services .blue { color: var(--blue); }
  .services .red { color: var(--red); }
  .headline {
    position: absolute; right: 20px; top: 232px; text-align: right;
    font-family: "Oswald", sans-serif; font-weight: 600; line-height: .98;
  }
  .headline .program { color: var(--blue); font-size: 54px; display: block; }
  .headline .product { color: var(--crimson); font-size: 54px; display: block; }
  .rate-title {
    position: absolute; right: 20px; top: 364px; width: 220px; text-align: center;
    color: #fff; font-weight: 700; font-size: 24px; line-height: 24px;
  }
  .rate-figure {
    position: absolute; right: 18px; top: 414px; height: 32px;
    color: #fff; font-weight: 700; font-size: 20px; line-height: 32px; white-space: nowrap;
  }
  .term {
    position: absolute; left: 42px; top: 376px; width: 110px; text-align: center;
    font-weight: 800; line-height: .9;
  }
  .term .years { color: var(--red); font-size: 34px; display: block; }
  .term .unit { color: var(--ink); font-size: 15px; display: block; }
  .benefits {
    position: absolute; right: 14px; top: 468px; text-align: right;
    color: var(--blue); font-weight: 700; font-size: 8.6px; line-height: 12.5px; text-transform: uppercase;
  }
  .benefits span::before { content: "\2022"; color: var(--red); margin: 0 3px 0 5px; }
  .footer {
    position: absolute; left: 0; bottom: 0; width: 405px; height: 56px; background: var(--mist);
  }
  .apply {
    position: absolute; left: 12px; top: 12px; width: 156px; height: 30px; border-radius: 7px;
    background: linear-gradient(180deg, var(--sky) 0%, var(--blue) 60%, var(--navy) 100%);
    color: #fff; font-weight: 700; font-size: 18px; line-height: 30px; text-align: center; letter-spacing: .5px;
  }
  .contact {
    position: absolute; left: 178px; top: 10px; color: var(--navy);
    font-weight: 700; font-size: 6.8px; line-height: 10px; text-transform: uppercase; white-space: nowrap;
  }
  .contact .row { display: flex; align-items: flex-start; gap: 4px; }
  .contact svg { flex: none; margin-top: 1px; }
  .divider { position: absolute; left: 334px; top: 8px; width: 1px; height: 38px; background: var(--red); }
  .license { position: absolute; left: 339px; top: 9px; width: 62px; text-align: center; }
  .pledge-mark { width: 18px; height: 16px; background: var(--ink); margin: 0 auto 7px; }
  .license-id { font-weight: 700; font-size: 6.6px; color: var(--ink); white-space: nowrap; }
</style>
</head>
<body>
<main class="flyer">
  <div class="hero-photo" role="img" aria-label="Photo of a model house with coin stacks, a jar of coins with a sprouting plant and a burlap money sack"></div>

  <svg class="shapes" width="405" height="573" viewBox="0 0 405 573">
    <defs>
      <linearGradient id="swoosh" x1="0" y1="0" x2="1" y2="0">
        <stop offset="0" stop-color="#e2183a"/>
        <stop offset=".45" stop-color="#8c1e5e"/>
        <stop offset="1" stop-color="#0455a3"/>
      </linearGradient>
      <linearGradient id="band-red" x1="0" y1="0" x2="1" y2="0">
        <stop offset="0" stop-color="#ec1f27"/>
        <stop offset="1" stop-color="#a50d1a"/>
      </linearGradient>
    </defs>
    <path d="M0 232 C40 250 75 300 96 338 C160 250 270 185 405 164 L405 573 L0 573 Z" fill="url(#swoosh)"/>
    <path d="M0 248 C42 266 76 312 96 350 C165 262 275 200 405 180 L405 573 L0 573 Z" fill="#d9dce2"/>
    <path d="M0 256 C44 276 78 322 96 362 C168 274 280 212 405 194 L405 573 L0 573 Z" fill="#ffffff"/>
    <polygon points="136,362 405,362 405,414 120,414" fill="url(#band-red)"/>
    <polygon points="120,414 405,414 405,446 106,446" fill="#0455a3"/>
    <polygon points="97,330 170,400 97,470 24,400" fill="#0455a3"/>
    <polygon points="97,342 158,400 97,458 36,400" fill="#ffffff"/>
    <polygon points="97,350 150,400 97,450 44,400" fill="#e4e6ea"/>
  </svg>

  <div class="brand"><span class="brand-mark"></span>Oakmere Capital</div>

  <div class="services">
    <div class="blue">HOME</div>
    <div class="blue">REFINANCE</div>
    <div class="red">RESIDENTIAL</div>
    <div class="red">MORTGAGES</div>
  </div>

  <h1 class="headline">
    <span class="program">VA IRRL</span>
    <span class="product">REFINANCE</span>
  </h1>

  <div class="term"><span class="years">30</span><span class="unit">YEAR</span></div>
  <div class="rate-title">FIXED RATES<br>AS LOW AS</div>
  <div class="rate-figure">2.25% | 2.437% APR</div>

  <p class="benefits">
    <span>No Appraisal</span><span>No Out of Pocket Cost</span><br>
    <span>No Income Verification</span><span>No Asset Verification</span><br>
    <span>Close in 30 Days or Less</span>
  </p>

  <footer class="footer">
    <div class="apply">APPLY NOW</div>
    <div class="contact">
      <div class="row">
        <svg width="7" height="9" viewBox="0 0 7 9"><path d="M3.5 0A3.5 3.5 0 0 0 0 3.5C0 6 3.5 9 3.5 9S7 6 7 3.5A3.5 3.5 0 0 0 3.5 0Z" fill="#ec1f27"/><circle cx="3.5" cy="3.5" r="1.3" fill="#fff"/></svg>
        <div>4817B Wellsbury Road,<br>Alexandria, VA 22987</div>
      </div>
      <div class="row" style="margin-top:3px">
        <svg width="7" height="7" viewBox="0 0 8 8"><circle cx="4" cy="4" r="3.4" fill="none" stroke="#ec1f27" stroke-width="1"/><path d="M.6 4H7.4M4 .6C2 3 2 5 4 7.4M4 .6C6 3 6 5 4 7.4" fill="none" stroke="#ec1f27" stroke-width=".8"/></svg>
        <div>www.oakmerecapital-demo.com</div>
      </div>
    </div>
    <div class="divider"></div>
    <div class="license">
      <div class="pledge-mark" aria-label="Bright Harbor Pledge"></div>
      <div class="license-id">QRLA 5830724</div>
    </div>
  </footer>
</main>
</body>
</html>
```